Commercial Diving Company, Needs website designed and coded

We need a website designed for a new commercial diving company based on vancouver island. We fix docks using styrofoam billets installed underwater, as well as surveys, inspections, and plan to move into the aquaculture industry. Our main focus at the moment is flotation and want our customers to have an easy to navigate web page to answer their questions so they can understand a little more about what our service provides. We would like to see our main logo colours (blue/yellow) . The final design should communicate Safety, Success, and trustworthy work.

Target Market(s)

Fishing lodges, Fish Farms, Marinas, Logging Camps, Float home owners, Lake House owners

Coding

Coded - Design and coding required

Number of Pages Required

3 page

Font styles to use
Sans Serif

Colors
3277b5
fbed22
85cae6
ffffff
fbf289
00a990

Requirements
Must have
• Pages: about us, services offered, link to facebook, contact us - with link to email, phone

Book a free quote tab

```html
<!DOCTYPE html>
<html lang="en">
<head>
<meta charset="utf-8">
<title>Tidewell Dive Services</title>
<link href="https://fonts.googleapis.com/css2?family=Poppins:wght@400;500;600;700&display=swap" rel="stylesheet">
<style>
:root{
  --blue:#1f67b4;
  --blue-deep:#15549a;
  --link-blue:#2a63b0;
  --yellow:#f3c637;
  --ink:#222;
  --muted:#7a7a7a;
  --dark:#2a2727;
  --panel:#383535;
  --white:#fff;
  --social-a:#3b5998;
  --social-b:#2ea7df;
  --social-c:#e52424;
}
*{box-sizing:border-box;margin:0;padding:0}
html,body{width:1200px;height:2584px;overflow:hidden}
body{font-family:'Poppins',sans-serif;color:var(--ink);position:relative;background:var(--white)}
.abs{position:absolute}
a{text-decoration:none;color:inherit}
.btn{position:absolute;display:flex;align-items:center;justify-content:center;gap:10px;background:var(--yellow);color:#222;border-radius:22px;font-size:12px;font-weight:600}
.btn svg{width:13px;height:13px}

/* header */
.site-header{position:absolute;top:0;left:0;width:1200px;height:80px;background:var(--white);z-index:3}
.nav a{position:absolute;top:32px;font-size:12px;color:#333}
.nav a.active{color:var(--link-blue)}
.header-call{position:absolute;left:750px;top:31px;font-size:13px;font-weight:600;display:flex;align-items:center;gap:5px}
.header-call svg{width:18px;height:18px}
.brand-badge{position:absolute;left:510px;top:-40px;width:180px;height:180px;border-radius:50%;background:var(--white);z-index:4;display:flex;align-items:center;justify-content:center;padding-top:40px}
.brand-name{font-size:14px;font-weight:600;color:var(--blue);text-align:center;line-height:1.2}

/* hero */
.hero{position:absolute;top:80px;left:0;width:1200px;height:560px;background:linear-gradient(110deg,#6d8bb0 0%,#2c4468 30%,#20283a 55%,#3a3f4a 75%,#1f2a3d 100%)}
.hero h1{position:absolute;top:226px;left:0;width:1200px;text-align:center;color:var(--white);font-size:30px;font-weight:600;line-height:35px}
.hero .arrow{position:absolute;top:270px;width:18px;height:18px}
.hero .down{position:absolute;left:594px;top:504px;width:12px;height:12px}

/* services */
.eyebrow{color:var(--yellow);font-size:15px;font-weight:500}
.h2{font-size:30px;font-weight:500;color:var(--ink)}
.h2-sub{font-size:19px;font-weight:500}
.body-copy{font-size:12px;line-height:19px;color:var(--muted)}
.service-card{position:absolute;top:843px;width:280px;height:280px;box-shadow:0 4px 14px rgba(0,0,0,.08);background:var(--white)}
.service-card .media{height:200px}
.service-card .caption{height:80px;padding:18px 23px;font-size:15px;font-weight:500;line-height:22px;display:flex;justify-content:space-between;align-items:center}
.service-card.is-active .caption{color:var(--link-blue)}
.service-card.is-active svg{width:14px;height:14px}
.service-card.is-plain .caption{background:var(--yellow);color:#222}

/* about */
.about{position:absolute;top:1188px;left:0;width:1200px;height:560px;background:linear-gradient(135deg,var(--blue) 0%,var(--blue-deep) 100%)}
.about-text{position:absolute;left:612px;top:92px;width:360px;color:var(--white)}
.about-text h2{font-size:40px;font-weight:600;line-height:44px;margin-top:22px}
.about-text h3{font-size:25px;font-weight:500;line-height:30px}
.about-text p{font-size:12px;line-height:19.3px;margin-top:22px}

/* why */
.center{position:absolute;left:0;width:1200px;text-align:center}
.reason{position:absolute;top:1945px;width:240px;text-align:center}
.reason svg{width:50px;height:50px;margin-bottom:10px}
.reason h4{font-size:15px;font-weight:500;margin-bottom:10px}

/* footer */
.site-footer{position:absolute;top:2160px;left:0;width:1200px;height:424px;background:var(--dark);color:var(--white)}
.site-footer h5{font-size:15px;font-weight:500}
.quick a{display:block;font-size:12px;line-height:24px;color:#ddd}
.social{position:absolute;top:240px;width:40px;height:40px;border-radius:50%}
.quote-panel{position:absolute;left:688px;top:32px;width:356px;height:360px;background:var(--panel)}
.quote-panel h5{text-align:center;font-size:20px;font-weight:500;line-height:25px;margin-top:30px}
.field{position:absolute;border:1px solid #8a8787;border-radius:20px;font-size:10.5px;color:#ddd;padding:0 18px;display:flex;align-items:center}
</style>
</head>
<body>

<header class="site-header">
  <nav class="nav">
    <a class="active" style="left:136px">Home</a>
    <a style="left:216px">About Us</a>
    <a style="left:313px">Services</a>
    <a style="left:407px">Contact</a>
  </nav>
  <div class="header-call">Call.
    <svg viewBox="0 0 20 20"><circle cx="10" cy="10" r="9" fill="none" stroke="#f3c637" stroke-width="1.5"/><path d="M7 5.5l1.6 2.4-1 1.2c.6 1.3 1.5 2.2 2.6 2.8l1.2-1 2.4 1.6-.9 1.8c-3.3-.2-6.4-3.4-6.6-6.9z" fill="#f3c637"/></svg>
    <span style="font-weight:500">1.800.555.0142</span></div>
  <a class="btn" style="left:936px;top:20px;width:120px;height:40px">Get A Quote</a>
</header>
<div class="brand-badge"><div class="brand-name">Tidewell<br>Dive Services</div></div>

<section class="hero" role="img" aria-label="Commercial divers in helmets and dive gear on a dock beside the water">
  <h1>Providing professional commercial<br>diving services nationwide</h1>
  <svg class="arrow" style="left:57px" viewBox="0 0 18 18"><path d="M12 2L5 9l7 7" fill="none" stroke="#fff" stroke-width="2.4"/></svg>
  <svg class="arrow" style="left:1125px" viewBox="0 0 18 18"><path d="M6 2l7 7-7 7" fill="none" stroke="#fff" stroke-width="2.4"/></svg>
  <a class="btn" style="left:504px;top:320px;width:193px;height:40px">Contact Us Today!
    <svg viewBox="0 0 14 14"><path d="M1 7h11M8 3l4 4-4 4" fill="none" stroke="#222" stroke-width="1.4"/></svg></a>
  <svg class="down" viewBox="0 0 12 12"><path d="M1 4l5 5 5-5" fill="none" stroke="#fff" stroke-width="1.8"/></svg>
</section>

<section class="services">
  <div class="abs eyebrow" style="left:232px;top:701px">Our Services</div>
  <div class="abs h2" style="left:232px;top:742px">Big or Small</div>
  <div class="abs h2-sub" style="left:232px;top:782px">Tidewell Dive Services does it all!</div>
  <p class="abs body-copy" style="left:612px;top:746px;width:350px">Lorem ipsum dolor sit amet, consectetur adipiscing elit, sed do eiusmod tempor incididunt ut labore et dolore magna aliqua.</p>

  <article class="service-card is-active" style="left:155px">
    <div class="media" role="img" aria-label="Floating wooden dock on the water" style="background:linear-gradient(160deg,#4a6680,#8c8f92 55%,#3c4e5e)"></div>
    <div class="caption"><span>Fix Dock Using Billet<br>Installation</span>
      <svg viewBox="0 0 14 14"><path d="M1 7h11M8 3l4 4-4 4" fill="none" stroke="#2a63b0" stroke-width="1.4"/></svg></div>
  </article>
  <article class="service-card is-plain" style="left:460px">
    <div class="media" role="img" aria-label="Divers inspecting a structure underwater" style="background:linear-gradient(150deg,#2ec6c8,#1aa7a9 50%,#3d5a3e)"></div>
    <div class="caption"><span>Underwater Inspections<br>and Survey</span></div>
  </article>
  <article class="service-card is-plain" style="left:764px">
    <div class="media" role="img" aria-label="Commercial diver in helmet waving from the water" style="background:linear-gradient(160deg,#e8eef2,#b8c3c8 50%,#3a3d44)"></div>
    <div class="caption"><span>Commercial<br>Diving</span></div>
  </article>
</section>

<section class="about">
  <svg class="abs" style="left:80px;top:48px" width="460" height="460" viewBox="0 0 460 460">
    <circle cx="228" cy="231" r="216" fill="#f4f6f9"/>
    <g fill="none" stroke="#fff" stroke-width="2.5">
      <circle cx="300" cy="22" r="9"/><circle cx="412" cy="54" r="10"/><circle cx="436" cy="112" r="6"/>
      <circle cx="368" cy="102" r="20" stroke-width="4"/><circle cx="20" cy="312" r="10"/><circle cx="90" cy="398" r="20" stroke-width="4"/>
      <circle cx="45" cy="436" r="6"/><circle cx="136" cy="342" r="10"/>
    </g>
  </svg>
  <div class="abs" role="img" aria-label="Dive supervisor in a hard hat reviewing plans with a crew member" style="left:176px;top:116px;width:316px;height:316px;border-radius:50%;background:linear-gradient(150deg,#5b6a7a,#2f343c 60%,#1d2128)"></div>
  <div class="about-text">
    <div class="eyebrow">About Company</div>
    <h2>Trusted Name</h2>
    <h3>Diving Services</h3>
    <p>Sed ut perspiciatis unde omnis iste natus error sit voluptatem accusantium doloremque laudantium, totam rem aperiam. Eaque ipsa quae ab illo inventore veritatis et quasi architecto beatae vitae dicta sunt explicabo. Nemo enim ipsam voluptatem quia voluptas sit aspernatur aut odit aut fugit, sed quia consequuntur magni dolores eos qui ratione voluptatem sequi nesciunt. Neque porro quisquam est, qui dolorem ipsum quia dolor sit amet, consectetur, adipisci velit, sed quia non numquam eius modi tempora.</p>
  </div>
  <a class="btn" style="left:612px;top:432px;width:128px;height:40px">About Us
    <svg viewBox="0 0 14 14"><path d="M1 7h11M8 3l4 4-4 4" fill="none" stroke="#222" stroke-width="1.4"/></svg></a>
</section>

<section class="why">
  <div class="center eyebrow" style="top:1808px">Why Choose Us</div>
  <div class="center h2" style="top:1846px">Reasons to Choose</div>
  <div class="center h2-sub" style="top:1888px">Tidewell Dive Services</div>

  <div class="reason" style="left:174px">
    <svg viewBox="0 0 50 50" fill="none" stroke="#f3c637" stroke-width="2"><rect x="12" y="4" width="30" height="42" rx="2"/><circle cx="14" cy="22" r="5"/><path d="M20 14h16M24 22h12M20 30h16M20 37h16M10 28v10l4-3 4 3V28"/></svg>
    <h4>Experienced</h4>
    <p class="body-copy">Duis aute irure dolor in reprehenderit in voluptate velit esse cillum dolore eu fugiat nulla pariatur.</p>
  </div>
  <div class="reason" style="left:480px">
    <svg viewBox="0 0 50 50" fill="none" stroke="#f3c637" stroke-width="2"><path d="M25 4l18 6v14c0 11-8 19-18 22C15 43 7 35 7 24V10z"/><path d="M17 25l6 6 11-12"/></svg>
    <h4>Trusted</h4>
    <p class="body-copy">Duis aute irure dolor in reprehenderit in voluptate velit esse cillum dolore eu fugiat nulla pariatur.</p>
  </div>
  <div class="reason" style="left:785px">
    <svg viewBox="0 0 50 50" fill="none" stroke="#f3c637" stroke-width="2"><path d="M14 18a11 11 0 0 1 22 0zM12 18h26M17 22v4a8 8 0 0 0 16 0v-4M8 46V38c0-4 4-6 8-6h18c4 0 8 2 8 6v8zM20 32l5 6 5-6"/></svg>
    <h4>Industry Leading</h4>
    <p class="body-copy">Duis aute irure dolor in reprehenderit in voluptate velit esse cillum dolore eu fugiat nulla pariatur.</p>
  </div>
</section>

<footer class="site-footer">
  <h5 class="abs" style="left:121px;top:58px">Need Help?</h5>
  <div class="abs" style="left:121px;top:92px;font-size:20px;font-weight:500">Call. <span style="color:var(--yellow)">1.800.555.0142</span></div>
  <div class="abs" style="left:121px;top:121px;font-size:12px;color:#ddd">E. hello@tidewelldive.com</div>
  <div class="abs" style="left:121px;top:160px;font-size:12px;line-height:19px;color:#ddd">Tidewell Dive Services<br>210 Harbour Lane, Nanaimo<br>BC V9R 2K8</div>
  <a class="social" aria-label="Social profile one" style="left:121px;background:var(--social-a)"></a>
  <a class="social" aria-label="Social profile two" style="left:169px;background:var(--social-b)"></a>
  <a class="social" aria-label="Video channel" style="left:217px;background:var(--social-c)"></a>
  <div class="abs" style="left:119px;top:336px;font-size:12px">©2020 Marlow Creative &nbsp;·&nbsp; All rights reserved</div>
  <div class="abs" style="left:119px;top:358px;font-size:10px;color:#aaa">Disclaimer &nbsp;·&nbsp; Privacy Policy &nbsp;·&nbsp; T&amp;C's</div>

  <h5 class="abs" style="left:460px;top:58px">Quick Link</h5>
  <div class="abs quick" style="left:460px;top:84px">
    <a>Home</a><a>About Us</a><a>Services</a><a>Contact</a><a>Get A Quote</a>
  </div>

  <form class="quote-panel">
    <h5>Get a Free Online<br>Quote Today!</h5>
    <div class="field" style="left:24px;top:96px;width:148px;height:40px">Name</div>
    <div class="field" style="left:184px;top:96px;width:148px;height:40px">Email</div>
    <div class="field" style="left:24px;top:148px;width:148px;height:40px">Phone</div>
    <div class="field" style="left:184px;top:148px;width:148px;height:40px">Subject</div>
    <div class="field" style="left:24px;top:200px;width:308px;height:80px;align-items:flex-start;padding-top:12px;border-radius:16px">Message</div>
    <a class="btn" style="left:130px;top:300px;width:96px;height:40px">Send
      <svg viewBox="0 0 14 14"><path d="M1 7h11M8 3l4 4-4 4" fill="none" stroke="#222" stroke-width="1.4"/></svg></a>
  </form>
</footer>

</body>
</html>
```